Kelbrook Aquatic Centre Open Day

FRONT PAGE

KELBROOK AQUATIC CENTRE OPEN DAY
31st May 2014
10am - 4pm
Free entry

Our Free Open Day is an event designed for the community to dive in and enjoy our great aquatic venue. There are plenty of activities for parents and kids to enjoy including the pool activities, free fitness classes and much more! Come join us on this great day to mark our 6 months of operation.

Sausage sizzle
pool activities
free group fitness classes
giveaways
door prizes

BACK PAGE
map of location
ph: 4731 5082
enquiries@kbaquatic-demo.com.au

want fitness and aquatic pics

plenty of colour - DL size
in your face kind of flyer

```html
<!DOCTYPE html>
<html lang="en">
<head>
<meta charset="utf-8">
<title>Kelbrook Aquatic Centre Open Day</title>
<link href="https://fonts.googleapis.com/css2?family=Bowlby+One&family=Michroma&family=Roboto+Condensed:wght@400;700&family=Roboto:wght@500&display=swap" rel="stylesheet">
<style>
  :root {
    --navy: #0b3a5c;
    --navy-deep: #06324f;
    --sky: #2aa7df;
    --sky-light: #5cc4ee;
    --teal: #3cb5c9;
    --aqua-text: #7fd3f5;
    --blue-deep: #0b4a9a;
    --blue-mid: #1a78cc;
    --blue-pale: #d8f1fc;
    --white: #ffffff;
  }
  html, body { margin: 0; padding: 0; overflow: hidden; }
  body { width: 1200px; height: 1000px; background: var(--white); }
  .flyer {
    position: relative; width: 1200px; height: 1000px; overflow: hidden;
    font-family: "Roboto Condensed", Arial, sans-serif;
    background: linear-gradient(118deg, var(--blue-deep) 0%, var(--blue-mid) 24%, var(--sky-light) 40%, var(--blue-pale) 52%, var(--white) 62%);
  }

  .brand {
    position: absolute; left: 440px; top: 108px; width: 340px;
    display: flex; align-items: center; gap: 14px;
  }
  .brand-dot { width: 26px; height: 26px; border-radius: 50%; background: var(--teal); flex: none; }
  .brand-name {
    font-family: "Roboto Condensed", Arial, sans-serif; font-weight: 700;
    color: var(--teal); font-size: 44px; line-height: 1.05; text-transform: uppercase;
  }

  .free-entry {
    position: absolute; left: 242px; top: 306px; padding: 4px 14px;
    background: var(--white); border: 2px solid var(--navy);
    color: var(--navy); font-size: 28px; font-family: "Roboto", Arial, sans-serif;
    transform: rotate(-9deg); box-shadow: 2px 3px 5px rgba(0,0,0,.3); z-index: 3;
  }
  .headline-open {
    position: absolute; left: 280px; top: 326px; width: 594px; margin: 0;
    font-family: "Bowlby One", Impact, sans-serif; font-size: 128px; line-height: 1;
    color: var(--navy); text-align: center; letter-spacing: 10px;
    transform: scaleX(1.42) scaleY(.9); transform-origin: center;
    z-index: 2;
  }
  .headline-day {
    position: absolute; left: 290px; top: 446px; width: 580px; height: 120px;
    background: var(--navy); z-index: 2; overflow: hidden;
  }
  .headline-day span {
    position: absolute; left: 118px; top: -14px;
    font-family: "Bowlby One", Impact, sans-serif; font-size: 128px; line-height: 1;
    letter-spacing: 12px; transform: scaleX(1.3) scaleY(.86); transform-origin: left;
    background: linear-gradient(90deg, var(--white) 10%, var(--sky-light) 60%, var(--white));
    -webkit-background-clip: text; background-clip: text; color: transparent;
  }

  .photo {
    position: absolute; border: 5px solid var(--white);
    box-shadow: 3px 4px 8px rgba(0,0,0,.45); z-index: 1;
  }
  .photo-gym { left: 36px; top: 392px; width: 240px; height: 175px; transform: rotate(-4deg);
    background: linear-gradient(160deg, #8a8276, #5b534a 60%, #3b3631); }
  .photo-polo { left: 186px; top: 565px; width: 262px; height: 138px; transform: rotate(-3deg);
    background: linear-gradient(160deg, #9fe2f0, #2fb4d8 55%, #1d8fbf); z-index: 3; }
  .photo-trainer { left: 892px; top: 376px; width: 236px; height: 142px; transform: rotate(-4deg);
    background: linear-gradient(160deg, #f4f4f4, #dcdcdc 60%, #bdbdbd); }
  .photo-swim { left: 742px; top: 535px; width: 250px; height: 162px; transform: rotate(-3deg);
    background: linear-gradient(160deg, #bff0fb, #54c8ea 55%, #2aa5d8); z-index: 3; }

  .when {
    position: absolute; left: 430px; top: 590px; width: 320px; margin: 0; text-align: center;
    font-family: Arial, Helvetica, sans-serif; font-weight: 700; color: var(--navy-deep);
    font-size: 40px; line-height: 48px; text-shadow: 0 0 6px #b8e8fb, 0 0 3px #fff; z-index: 2;
  }

  .tag {
    position: absolute; height: 50px; display: flex; align-items: center; justify-content: center;
    border: 1px solid rgba(255,255,255,.8); font-size: 28px; box-sizing: border-box;
  }
  .tag-dark { background: var(--navy); color: var(--aqua-text); }
  .tag-light { background: var(--sky); color: var(--navy-deep); }
  .address {
    left: 123px; top: 715px; width: 968px; font-family: "Michroma", Arial, sans-serif;
    font-size: 24px; letter-spacing: 1px;
  }
  .t1 { left: 63px; top: 774px; width: 350px; }
  .t2 { left: 415px; top: 776px; width: 368px; }
  .t3 { left: 785px; top: 776px; width: 356px; }
  .t4 { left: 219px; top: 829px; width: 311px; }
  .t5 { left: 692px; top: 829px; width: 311px; }
  .closing { left: 75px; top: 903px; width: 1052px; height: 61px; font-size: 35px; }
</style>
</head>
<body>
<main class="flyer">
  <div class="brand">
    <span class="brand-dot"></span>
    <span class="brand-name">Kelbrook Aquatic Centre</span>
  </div>

  <div class="photo photo-gym" role="img" aria-label="Trainer guiding a member through a gym workout"></div>
  <div class="photo photo-trainer" role="img" aria-label="Personal trainer assisting a client with dumbbells"></div>

  <div class="free-entry">Free Entry</div>
  <h1 class="headline-open">OPEN</h1>
  <div class="headline-day"><span>DAY</span></div>

  <div class="photo photo-polo" role="img" aria-label="Water polo player raising a ball in the pool"></div>
  <div class="photo photo-swim" role="img" aria-label="Swimmer doing freestyle in a lap pool"></div>

  <p class="when">31st May 2014<br>10am - 4pm</p>

  <div class="tag tag-light address">14 Harlow street kelbrook</div>
  <div class="tag tag-dark t1">Free group fitness classes</div>
  <div class="tag tag-light t2">Sausage sizzle</div>
  <div class="tag tag-dark t3">Pool activities</div>
  <div class="tag tag-light t4">Giveaways</div>
  <div class="tag tag-light t5">Door prizes</div>
  <div class="tag tag-dark closing">Come join us on this great day to mark our 6 months of operation.</div>
</main>
</body>
</html>
```